Law Firm Website

We are looking to update our old, tired and very flat website. We have someone who will code and host the site but we need some design inspiration. The website will consist of no more than 2/3 pages, possibly with pop-ups for information. We already have all the blurb. We would like something distinctive, clean and eye-catching, using the purple and white theme that we already use on our firm stationery. Examples uploaded. Current website URL is www.dunmorewillett.example.

Industry/Entity Type

Law Firm

```html
<!DOCTYPE html>
<html lang="en">
<head>
<meta charset="utf-8">
<title>Dunmore &amp; Willett Solicitors</title>
<link href="https://fonts.googleapis.com/css2?family=Figtree:wght@400;500;600;700&display=swap" rel="stylesheet">
<style>
:root{
  --header:#3f2752;
  --header-dark:#35203f;
  --purple:#5a3a78;
  --purple-mid:#6c4890;
  --title:#4f3470;
  --gold:#c9b062;
  --white:#ffffff;
  --text:#1e1a22;
  --muted:#a39fa6;
  --lilac:#cdb8e6;
  --footer:#3a2350;
}
*{margin:0;padding:0;box-sizing:border-box}
html,body{width:1200px;height:1156px;overflow:hidden}
body{position:relative;font-family:"Figtree",Arial,sans-serif;background:var(--footer);color:var(--white)}
.abs{position:absolute}

/* header */
.site-header{position:absolute;left:0;top:0;width:1200px;height:152px;background:radial-gradient(ellipse at 270px 70px,#4b3060 0%,var(--header) 45%,var(--header-dark) 100%);border-top:5px solid #56397a;border-bottom:4px solid #6a4893}
.brand{position:absolute;left:161px;top:54px;font-size:34px;font-weight:500;letter-spacing:-.5px;white-space:nowrap}
.brand-sub{position:absolute;left:163px;top:100px;font-size:13px;letter-spacing:11px;font-weight:500}
.pill{position:absolute;top:31px;height:39px;background:#46305a;border:1px solid #2e1c3c;border-radius:2px;box-shadow:inset 0 1px 0 rgba(255,255,255,.08);display:flex;align-items:center;justify-content:center;gap:8px;padding:0 12px;font-size:14px;letter-spacing:-.3px;white-space:nowrap}
.pill svg{flex:none}
.nav-rule{position:absolute;left:494px;top:92px;width:583px;height:1px;background:rgba(255,255,255,.12)}
.main-nav{position:absolute;top:92px;left:494px;width:583px;height:56px;display:flex;font-size:11px;font-weight:700;text-transform:uppercase;white-space:nowrap}
.main-nav a{color:var(--white);text-decoration:none;display:flex;align-items:center;justify-content:center;position:relative}
.main-nav a+a::before{content:"";position:absolute;left:0;top:12px;bottom:12px;width:1px;background:rgba(255,255,255,.12)}
.main-nav a.current::after{content:"";position:absolute;left:20px;right:20px;bottom:0;height:2px;background:var(--gold)}

/* hero */
.hero{position:absolute;left:0;top:152px;width:1200px;height:385px;background:var(--white);overflow:hidden}
.hero-photo{position:absolute;left:600px;top:0;width:600px;height:385px;background:linear-gradient(90deg,#fff 0%,#d9ced6 22%,#8f8189 60%,#5f535a 100%)}
.hero-title{position:absolute;left:155px;top:70px;font-size:37px;font-weight:500;color:var(--title);letter-spacing:-.3px;white-space:nowrap}
.hero-tag{position:absolute;left:156px;top:114px;font-size:33px;font-weight:500;color:var(--gold);letter-spacing:-.2px;white-space:nowrap}
.hero-rule{position:absolute;left:157px;top:160px;width:403px;height:1px;background:var(--gold)}
.hero-lead{position:absolute;left:158px;top:172px;width:420px;font-size:16px;line-height:25px;color:var(--text)}
.hero-reg{position:absolute;left:158px;top:246px;width:460px;font-size:13.5px;line-height:25px;color:var(--muted)}

/* middle band */
.panel{position:absolute;left:0;top:537px;width:1200px;height:431px;background:linear-gradient(180deg,#7a519e 0%,var(--purple-mid) 35%,var(--purple) 100%);box-shadow:inset 0 6px 10px rgba(0,0,0,.25)}
.col-head{position:absolute;width:216px;text-align:center;font-size:19px;font-weight:700;letter-spacing:-.3px;padding-bottom:7px;border-bottom:2px solid var(--gold)}
.small{font-size:12px}
.testimonial-photo{position:absolute;left:167px;top:117px;width:223px;height:122px;background:#fff;padding:4px}
.testimonial-photo div{width:100%;height:100%;background:linear-gradient(135deg,#e8e4dc,#b8c9dc 55%,#6f8fb4)}
.quote{position:absolute;left:171px;top:254px;width:216px;text-align:center;font-size:12px;line-height:16px}
.badge{position:absolute;left:169px;top:322px;width:141px;height:44px;background:#fff;border-radius:2px}
.expertise{position:absolute;left:500px;top:82px;width:206px;list-style:none}
.expertise li{height:55px;display:flex;align-items:center;gap:13px;font-size:16px;border-bottom:1px solid rgba(255,255,255,.12);padding-left:12px;white-space:nowrap}
.see-all{position:absolute;left:495px;top:366px;width:216px;text-align:center;font-size:12px}
.see-all span{color:var(--gold)}
.contact{position:absolute;left:760px;top:86px;width:250px;text-align:right;font-size:12px;line-height:18px;font-style:normal;white-space:nowrap}
.contact strong{font-size:14px;display:block;margin-bottom:2px}
.contact-rule{position:absolute;left:822px;top:239px;width:212px;height:1px;background:rgba(255,255,255,.15)}
.map{position:absolute;left:808px;top:256px;width:223px;height:123px;background:#fff;padding:3px}
.map div{width:100%;height:100%;background:linear-gradient(160deg,#e6e2da,#d9d4cb 60%,#cfd9c5)}

/* divider stripe */
.stripe{position:absolute;left:0;top:968px;width:1200px;height:20px;background:repeating-linear-gradient(135deg,#4a2f63 0 2px,#3f2756 2px 4px);border-top:1px solid #6a4893}

/* footer */
.foot-nav{position:absolute;left:157px;top:1031px;display:flex;gap:12px;font-size:13px;font-weight:700;color:var(--lilac);text-transform:uppercase;letter-spacing:-.2px;white-space:nowrap}
.foot-nav i{font-style:normal;color:var(--gold)}
.foot-text{position:absolute;left:157px;font-size:10px;color:#e9e1f2;letter-spacing:-.1px;white-space:nowrap}
.foot-brand{position:absolute;left:828px;top:1038px;font-size:34px;font-weight:500;color:#5e4578;letter-spacing:-.5px;white-space:nowrap}
.foot-brand-sub{position:absolute;left:830px;top:1086px;font-size:13px;letter-spacing:11px;font-weight:500;color:#5e4578}
</style>
</head>
<body>

<header class="site-header">
  <div class="brand">Dunmore &amp; Willett</div>
  <div class="brand-sub">SOLICITORS</div>

  <div class="pill" style="left:614px;width:150px">
    <svg width="14" height="14" viewBox="0 0 24 24"><circle cx="12" cy="12" r="10.5" fill="none" stroke="#c9b062" stroke-width="1.8"/><path d="M8.5 7.5l2 2-1 1.5c.7 1.4 1.8 2.5 3.2 3.2l1.5-1 2 2-1.4 1.6c-3.6-.4-7.3-4.1-7.6-7.7z" fill="#c9b062"/></svg>
    0333-555-0148
  </div>
  <div class="pill" style="left:774px;width:294px;font-size:12.5px">
    <svg width="18" height="13" viewBox="0 0 18 13"><rect x="1" y="1" width="16" height="11" fill="none" stroke="#c9b062" stroke-width="1.5"/><path d="M1 1l8 6 8-6" fill="none" stroke="#c9b062" stroke-width="1.5"/></svg>
    daniel.dunmore@dunmorewillett.example
  </div>

  <div class="nav-rule"></div>
  <nav class="main-nav">
    <a class="current" href="#" style="width:68px">Home</a>
    <a href="#" style="width:164px">Areas of Expertice</a>
    <a href="#" style="width:118px">Daniel Dunmore</a>
    <a href="#" style="width:116px">Peter Willett</a>
    <a href="#" style="width:117px">Contact Us</a>
  </nav>
</header>

<section class="hero">
  <div class="hero-photo" role="img" aria-label="Black and white photograph of a Gothic court building"></div>
  <h1 class="hero-title">Dunmore &amp; Willett Solicitors</h1>
  <div class="hero-tag">For The Service You Deserve</div>
  <div class="hero-rule"></div>
  <p class="hero-lead">We are a Firm of Solicitors with offices in Hartwell,<br>London and Kelbrook, Hertfordshire.</p>
  <p class="hero-reg">This Firm is authorised and regulated by the Solicitors&nbsp; Regulation Authority No.600318, VAT registered number: 700 1234 56</p>
</section>

<section class="panel">
  <h2 class="col-head" style="left:171px;top:32px">Testimonials</h2>
  <p class="abs small" style="left:171px;top:93px;width:218px;text-align:center">What OUR Clients Are Saying</p>
  <div class="testimonial-photo"><div role="img" aria-label="Photograph of a smiling family on a sofa"></div></div>
  <p class="quote">“ Thank you, thank you, thank you.<br>Your hard work and dedication has<br>changed my life for the better”</p>
  <div class="badge" role="img" aria-label="Partner membership badge"></div>

  <h2 class="col-head" style="left:495px;top:32px">Our Expertise</h2>
  <ul class="expertise">
    <li><svg width="12" height="12" viewBox="0 0 12 12"><circle cx="6" cy="6" r="6" fill="#c9b062"/><path d="M3.3 6.2l1.8 1.7 3.6-3.6" fill="none" stroke="#6c4890" stroke-width="1.5"/></svg>Company Matters</li>
    <li><svg width="12" height="12" viewBox="0 0 12 12"><circle cx="6" cy="6" r="6" fill="#c9b062"/><path d="M3.3 6.2l1.8 1.7 3.6-3.6" fill="none" stroke="#6c4890" stroke-width="1.5"/></svg>Commercial Matters</li>
    <li><svg width="12" height="12" viewBox="0 0 12 12"><circle cx="6" cy="6" r="6" fill="#c9b062"/><path d="M3.3 6.2l1.8 1.7 3.6-3.6" fill="none" stroke="#6c4890" stroke-width="1.5"/></svg>Commercial Crime</li>
    <li><svg width="12" height="12" viewBox="0 0 12 12"><circle cx="6" cy="6" r="6" fill="#c9b062"/><path d="M3.3 6.2l1.8 1.7 3.6-3.6" fill="none" stroke="#6c4890" stroke-width="1.5"/></svg>Litigations/ Disputes</li>
    <li><svg width="12" height="12" viewBox="0 0 12 12"><circle cx="6" cy="6" r="6" fill="#c9b062"/><path d="M3.3 6.2l1.8 1.7 3.6-3.6" fill="none" stroke="#6c4890" stroke-width="1.5"/></svg>Insolvency</li>
  </ul>
  <p class="see-all">See All <span>»</span></p>

  <h2 class="col-head" style="left:812px;top:32px">Contact Us</h2>
  <address class="contact">
    <strong>Daniel Dunmore</strong>
    42b Larchfield Road<br>Hartwell<br>London NW9 4QT<br>
    <span style="display:block;margin-top:8px">Tel:&nbsp; 0333 555 0148<br>Fax: 020 7946 0321</span>
    <span style="display:block;margin-top:5px">daniel.dunmore@dunmorewillett.example</span>
  </address>
  <div class="contact-rule"></div>
  <div class="map"><div role="img" aria-label="Street map showing the office location"></div></div>
</section>

<div class="stripe"></div>

<footer>
  <nav class="foot-nav">
    <span>Home</span><i>/</i><span>Areas of Exertise</span><i>/</i><span>Daniel Dunmore</span><i>/</i><span>Peter Willett</span><i>/</i><span>Contact Us</span>
  </nav>
  <p class="foot-text" style="top:1062px">© Copyright 2014 &nbsp; Dunmore + Willett Solicitors &nbsp; | &nbsp; Legal Notices &nbsp; | &nbsp; Privacy Policy</p>
  <p class="foot-text" style="top:1083px">Also at 12 The Avenue, Kelbrook, Hertfordshire AL9 2XY and The Wharf, Mill Farm Lane, Easterby, Essex CM9 4ZZ</p>
  <p class="foot-text" style="top:1103px">This Firm is Authorised and Regulated by the Solicitors Regulation Authority, Number 600318</p>
  <div class="foot-brand">Dunmore &amp; Willett</div>
  <div class="foot-brand-sub">SOLICITORS</div>
</footer>

</body>
</html>
```